Name and logo for Ember Fitness Coaching LLC
Ember Fitness Coaching
Name and logo for Ember Fitness Coaching LLC - Health
Creative Brief
Simple
Dale Whitmore
Owner
Marlow, NE
dale@emberfitnesscoaching-example.com
emberfitnesscoaching-example.com

```html
<!DOCTYPE html>
<html lang="en">
<head>
<meta charset="utf-8">
<title>Ember Fitness Coaching – Business Card</title>
<link rel="stylesheet" href="https://fonts.googleapis.com/css2?family=Open+Sans:wght@400;600;700&display=swap">
<style>
  :root {
    --backdrop: #d8d8d9;
    --card-white: #ffffff;
    --ember-orange: #f4793a;
    --ember-red: #e3403d;
    --text-dark: #555556;
    --text-muted: #8a8a8a;
  }
  * { box-sizing: border-box; margin: 0; padding: 0; }
  html, body { width: 1200px; height: 899px; overflow: hidden; }
  body {
    background: var(--backdrop);
    font-family: "Open Sans", Arial, sans-serif;
    position: relative;
  }
  .card {
    position: absolute;
    width: 540px;
    height: 309px;
    border-radius: 2px;
    box-shadow: 0 6px 18px rgba(0,0,0,0.18);
  }
  /* back side */
  .card--back {
    left: 150px;
    top: 110px;
    background: linear-gradient(200deg, var(--ember-orange) 0%, var(--ember-red) 100%);
    display: flex;
    align-items: center;
    justify-content: center;
    gap: 22px;
    color: var(--card-white);
  }
  .back-mark {
    display: flex;
    align-items: center;
    gap: 10px;
    font-weight: 700;
    font-size: 17px;
  }
  .mark-dot {
    width: 14px; height: 14px;
    border-radius: 50%;
    background: currentColor;
    flex: none;
  }
  .back-url {
    font-size: 11px;
    letter-spacing: 0.5px;
  }
  /* front side */
  .card--front {
    left: 510px;
    top: 470px;
    background: var(--card-white);
  }
  .contact {
    position: absolute;
    left: 34px;
    top: 100px;
    width: 260px;
  }
  .contact__name {
    color: var(--ember-red);
    font-weight: 700;
    font-size: 17px;
    line-height: 1.1;
  }
  .contact__role {
    color: var(--text-muted);
    font-size: 10px;
    margin-bottom: 12px;
  }
  .contact__address {
    color: var(--text-dark);
    font-size: 11px;
    line-height: 1.45;
    margin-bottom: 6px;
  }
  .contact__list { list-style: none; }
  .contact__item {
    display: flex;
    align-items: center;
    gap: 8px;
    color: var(--text-dark);
    font-size: 11px;
    line-height: 1.9;
    white-space: nowrap;
  }
  .contact__icon { width: 11px; height: 11px; flex: none; }
  .front-mark {
    position: absolute;
    right: 30px;
    top: 150px;
    display: flex;
    align-items: center;
    gap: 8px;
    color: var(--ember-red);
    font-weight: 700;
    font-size: 16px;
    white-space: nowrap;
  }
</style>
</head>
<body>
  <section class="card card--back" aria-label="Business card back">
    <div class="back-mark"><span class="mark-dot"></span>Ember Fitness Coaching</div>
    <p class="back-url">www.emberfitnesscoaching-example.com</p>
  </section>

  <section class="card card--front" aria-label="Business card front">
    <div class="contact">
      <h1 class="contact__name">Dale Whitmore</h1>
      <p class="contact__role">Owner</p>
      <p class="contact__address">Lorem ipsum dolor sit<br>amet, Marlow, NE</p>
      <ul class="contact__list">
        <li class="contact__item">
          <svg class="contact__icon" viewBox="0 0 12 12"><circle cx="6" cy="6" r="6" fill="#e3403d"/><rect x="4" y="2.5" width="4" height="7" rx="0.8" fill="#fff"/></svg>
          555-380-0164
        </li>
        <li class="contact__item">
          <svg class="contact__icon" viewBox="0 0 12 12"><circle cx="6" cy="6" r="6" fill="#e3403d"/><rect x="3" y="4" width="6" height="4.2" fill="#fff"/><path d="M3 4 L6 6.3 L9 4" stroke="#e3403d" stroke-width="0.7" fill="none"/></svg>
          dale@emberfitnesscoaching-example.com
        </li>
        <li class="contact__item">
          <svg class="contact__icon" viewBox="0 0 12 12"><circle cx="6" cy="6" r="6" fill="#e3403d"/><circle cx="6" cy="6" r="3" stroke="#fff" stroke-width="0.9" fill="none"/><line x1="3" y1="6" x2="9" y2="6" stroke="#fff" stroke-width="0.7"/></svg>
          www.emberfitnesscoaching-example.com
        </li>
      </ul>
    </div>
    <div class="front-mark"><span class="mark-dot"></span>Ember Fitness Coaching</div>
  </section>
</body>
</html>
```